Brand design for Varundel Partners

We are a new start up Fund Manager based in Singapore in need of a stylish and slick corporate identity starting with letterhead and business card (2 separate projects on craft hive but must be completed as one). We are aiming to be a somewhat 'budget' service provider with a target market of high net worth individuals and savvy self traders so we need to have our look convey value but with style. Our logo is attached and the use of the blue is imperative. The company name is Varundel Partners Pte Ltd and the verbiage 'Licensed by the Financial Oversight Board of Singapore - RFMC licence no. QRT804217-3' should be incorporated in small print.

Business card should also include address, office, direct and mobile numbers as well as email address. Follow me on twitter/fb/linkedin/Google+ should also be incrorporated. We are also looking to have a QR code on the business card that people can read with a smartphone which will auto populate our contact details in to their address book.

Many thanks and happy designing!

Reason: Extending so we can have further internal discussions. Thanks for input so far, some great designs coming through! Cheers

```html
<!DOCTYPE html>
<html lang="en">
<head>
<meta charset="utf-8">
<meta name="format-detection" content="telephone=no">
<title>Varundel Partners – Letterhead</title>
<link rel="stylesheet" href="https://fonts.googleapis.com/css2?family=Arimo:wght@700&family=Open+Sans:wght@400;800&display=swap">
<style>
  :root {
    --band: #84a6cf;
    --band-edge: #5d86b9;
    --brand-blue: #1a4f9e;
    --icon: #1a1a1a;
    --ink: #111111;
    --paper: #ffffff;
    --frame: #2b5ea8;
  }
  * { box-sizing: border-box; margin: 0; padding: 0; }
  html, body { width: 840px; height: 1200px; overflow: hidden; background: var(--paper); }
  .canvas { position: relative; width: 840px; height: 1200px; background: var(--paper); }

  .sheet {
    position: absolute; left: 4px; top: 4px; width: 832px; height: 1117px;
    border: 2px solid var(--frame);
  }
  .header-band {
    position: absolute; left: 0; top: 0; width: 100%; height: 144px;
    background: var(--band);
    border-bottom: 1px solid var(--band-edge);
  }
  .company-name {
    position: absolute; left: 14px; top: 54px;
    font-family: "Arimo", Arial, sans-serif; font-weight: 700;
    font-size: 33px; line-height: 36px; color: var(--brand-blue);
  }
  .contact-list {
    position: absolute; left: 398px; top: 13px; list-style: none;
    font-family: "Arimo", Arial, sans-serif; font-weight: 700;
    font-size: 26px; color: var(--brand-blue);
  }
  .contact-list li { display: flex; align-items: center; height: 30px; white-space: nowrap; }
  .contact-list svg { width: 40px; height: 24px; margin-right: 14px; flex: none; }
  .contact-list a, .contact-list span { color: inherit; text-decoration: none; }
  .licence-line {
    position: absolute; left: 6px; top: 150px; width: 818px;
    font-family: "Open Sans", Arial, sans-serif; font-weight: 800;
    font-size: 16.5px; line-height: 24px; color: var(--brand-blue);
    letter-spacing: -0.35px; white-space: nowrap;
  }
  .rule { position: absolute; left: 0; top: 176px; width: 100%; border-top: 2px solid var(--frame); }

  .caption {
    position: absolute; left: 0; top: 1126px; width: 840px; text-align: center;
    font-family: "Open Sans", Arial, sans-serif; font-weight: 400;
    font-size: 58px; line-height: 72px; color: var(--ink);
  }
</style>
</head>
<body>
<div class="canvas">
  <div class="sheet">
    <header class="header-band">
      <div class="company-name">Varundel<br>Partners Pte Ltd</div>
      <ul class="contact-list">
        <li>
          <svg viewBox="0 0 40 24" aria-hidden="true"><path d="M3 20 V10 Q20 2 37 10 V20 Z" fill="var(--icon)"/><rect x="14" y="9" width="12" height="4" fill="#ffffff"/></svg>
          <span>: Street # 57, Keppel Road</span>
        </li>
        <li>
          <svg viewBox="0 0 40 24" aria-hidden="true"><rect x="3" y="5" width="34" height="15" rx="2" fill="var(--icon)"/><rect x="13" y="9" width="14" height="4" fill="#84a6cf"/></svg>
          <span>: Street # 18-B, Orchard Lane</span>
        </li>
        <li>
          <svg viewBox="0 0 40 24" aria-hidden="true"><rect x="12" y="2" width="16" height="20" rx="2" fill="var(--icon)"/></svg>
          <span>: 6241&#8203; 9037 55</span>
        </li>
        <li>
          <svg viewBox="0 0 40 24" aria-hidden="true"><text x="20" y="19" text-anchor="middle" font-family="Arial, sans-serif" font-weight="700" font-size="22" fill="#1a1a1a">@</text></svg>
          <span>: info@varundel.com</span>
        </li>
      </ul>
    </header>
    <p class="licence-line">'Licensed by the Financial Oversight Board of Singapore - RFMC licence no. QRT804217-3'</p>
    <div class="rule"></div>
  </div>
  <p class="caption">Letter head design</p>
</div>
</body>
</html>
```